Business Card Design Project

We would like to have a new design for our Business Cards.
Please see attached JPEG to see the current.
We would like to be sober and clean, very professional.

Target Market(s)

IT Market

Industry/Entity Type

Business

Font styles to use
Serif
Sans Serif

Colors
ec1f27
f78f20
333333
5c5c5c
9d9d9d
e9e9e9
ffffff

Requirements
Must have
• It needs to be completely different than the current design (see attached),

```html
<!DOCTYPE html>
<html lang="en">
<head>
<meta charset="utf-8">
<title>NexaCore Business Card</title>
<link rel="stylesheet" href="https://fonts.googleapis.com/css2?family=PT+Serif:wght@400;700&family=Open+Sans:wght@400;600&display=swap">
<style>
  :root {
    --brand-red: #ec1f27;
    --brand-red-dark: #c8161d;
    --ink: #333333;
    --ink-soft: #5c5c5c;
    --grey-mid: #9d9d9d;
    --grey-light: #e9e9e9;
    --paper: #ffffff;
    --backdrop: #e4e4e4;
  }
  * { box-sizing: border-box; margin: 0; padding: 0; }
  html, body { width: 1200px; height: 1200px; overflow: hidden; }
  body {
    background: var(--backdrop);
    display: flex; align-items: center; justify-content: center;
  }
  .business-card {
    position: relative;
    width: 1000px; height: 572px;
    background: var(--paper);
    box-shadow: 0 10px 30px rgba(0,0,0,.18);
    overflow: hidden;
  }
  .card-top {
    position: absolute; left: 0; top: 0; width: 100%; height: 250px;
    background: linear-gradient(180deg, var(--paper) 0%, #f4f4f4 70%, var(--grey-light) 100%);
  }
  .holder {
    position: absolute; right: 48px; top: 34px; text-align: right;
  }
  .holder-name {
    font-family: "PT Serif", Georgia, serif;
    font-size: 40px; letter-spacing: 1px;
    color: var(--brand-red); line-height: 1.1;
  }
  .holder-title {
    font-family: "Open Sans", Arial, sans-serif;
    font-size: 30px; color: var(--ink); margin-top: 2px;
  }
  .brand {
    position: absolute; left: 56px; top: 150px;
    display: flex; align-items: center; gap: 26px;
  }
  .brand-mark {
    width: 96px; height: 96px; border-radius: 50%;
    background: var(--brand-red);
  }
  .brand-name {
    font-family: "PT Serif", Georgia, serif; font-weight: 700;
    font-size: 54px; color: var(--brand-red);
  }
  .card-band {
    position: absolute; left: 0; top: 250px; width: 100%; height: 200px;
    background: linear-gradient(180deg, var(--brand-red) 0%, var(--brand-red-dark) 100%);
    color: var(--paper);
    font-family: "PT Serif", Georgia, serif;
  }
  .address {
    position: absolute; left: 56px; top: 72px;
    display: flex; gap: 14px; font-size: 23px; line-height: 1.35;
  }
  .contacts {
    position: absolute; right: 48px; top: 26px;
    list-style: none; font-size: 24px;
  }
  .contacts li { display: flex; align-items: center; gap: 16px; margin-bottom: 12px; }
  .icon { width: 24px; height: 24px; flex: none; }
  .card-services {
    position: absolute; left: 0; top: 450px; width: 100%; height: 122px;
    background: linear-gradient(180deg, var(--grey-light) 0%, #d6d6d6 100%);
    display: flex; align-items: center; justify-content: center;
    text-align: center;
    font-family: "Open Sans", Arial, sans-serif;
    font-size: 25px; line-height: 1.35; color: var(--ink);
  }
</style>
</head>
<body>
  <article class="business-card">
    <section class="card-top">
      <div class="holder">
        <p class="holder-name">DANIEL REYES</p>
        <p class="holder-title">COO Mexico</p>
      </div>
      <div class="brand">
        <span class="brand-mark"></span>
        <span class="brand-name">NexaCore</span>
      </div>
    </section>

    <section class="card-band">
      <div class="address">
        <svg class="icon" viewBox="0 0 24 24" aria-hidden="true"><path fill="#fff" d="M12 2a7 7 0 0 0-7 7c0 5 7 13 7 13s7-8 7-13a7 7 0 0 0-7-7zm0 9.5A2.5 2.5 0 1 1 12 6.5a2.5 2.5 0 0 1 0 5z"/></svg>
        <p>Av. Alameda 482, Piso 7, Suite 3,<br>Colonia Jardines, San Pedro Garza Garcia,<br>N.L. Mexico 66210.</p>
      </div>
      <ul class="contacts">
        <li>
          <svg class="icon" viewBox="0 0 24 24" aria-hidden="true"><path fill="#fff" d="M6.6 10.8a15 15 0 0 0 6.6 6.6l2.2-2.2a1 1 0 0 1 1-.25 11.4 11.4 0 0 0 3.6.6 1 1 0 0 1 1 1V20a1 1 0 0 1-1 1A17 17 0 0 1 3 4a1 1 0 0 1 1-1h3.5a1 1 0 0 1 1 1c0 1.25.2 2.45.6 3.6a1 1 0 0 1-.25 1z"/></svg>
          +52 (81) 5550 4127
        </li>
        <li>
          <svg class="icon" viewBox="0 0 24 24" aria-hidden="true"><path fill="#fff" d="M2 5h20v14H2z"/><path fill="none" stroke="#c8161d" stroke-width="1.8" d="M2 5l10 8 10-8"/></svg>
          danielreyes@nexacore.com
        </li>
        <li>
          <svg class="icon" viewBox="0 0 24 24" aria-hidden="true"><g fill="none" stroke="#fff" stroke-width="1.8"><circle cx="12" cy="12" r="9.5"/><ellipse cx="12" cy="12" rx="4" ry="9.5"/><path d="M2.5 12h19M4 7h16M4 17h16"/></g></svg>
          www.nexacore.com
        </li>
      </ul>
    </section>

    <section class="card-services">
      <p>IT Consulting | Application Development &amp; Maintenance |<br>Business Process Outsourcing</p>
    </section>
  </article>
</body>
</html>
```